Hip-Hop Artist TM Blaze Needs a Album Cover Design

I need an album cover design for my upcoming album. I am a hip-hop artist from Seattle, WA. I have been writing/producing/releases music for the past 15 years. This will be my 4th full length album. For examples of my previous album cover designs and single designs go here --> www.tmblaze-music.net. The title of the album is called "Quiet Harbors". It is an emotional, inspirational album with 18 songs that I wrote and produced over the past 3 years. Some track titles include - "Hold Fast", "Golden Dust". "Kings of Tomorrow", "Burn The Ledger", & "Edge of Winter". I would like the cover to contain something design pattern based, 1 idea would be the blueprint design of a mind processing thoughts - abstract I know. But, feel free to think creatively or out of the box on this as I don't want to give too much direction - you are the graphic artist, not me. I have typically had blues, grays, and blacks in my album covers, but I don't want to put limits on the approach an artist wants to take. Feel free to take this in a direction you think would be interesting.

Reason: I would like to extend the deadline for design submissions in order to have time to provide appropriate feedback to the designers.

Reason: Thank you to everyone that has submitted designs thus far. I truly appreciate you taking the time and sharing your creativity. With the recent design submissions that came in today + the revisions sent yesterday/today, I would like to extend this contest by 5 days - as this album + design means the world to me. I will be providing feedback to the top designers tomorrow. Thank you all again!

```html
<!DOCTYPE html>
<html lang="en">
<head>
<meta charset="utf-8">
<title>Quiet Harbors — TM Blaze</title>
<link rel="stylesheet" href="https://fonts.googleapis.com/css2?family=Orbitron:wght@500&display=swap">
<style>
  :root {
    --page: #ffffff;
    --pale-blue: #dce9f2;
    --ice: #f2f7fb;
    --copper: #d9732e;
    --rust: #b4521c;
    --ink: #121212;
    --title-orange: #e8571a;
    --white: #ffffff;
  }
  html, body {
    margin: 0;
    width: 1200px;
    height: 900px;
    overflow: hidden;
    background: var(--page);
  }
  .album-cover {
    position: absolute;
    left: 200px;
    top: 50px;
    width: 800px;
    height: 800px;
    overflow: hidden;
  }
  .neural-backdrop {
    position: absolute;
    inset: 0;
    background:
      radial-gradient(ellipse at 30% 25%, rgba(217,115,46,0.35), transparent 55%),
      radial-gradient(ellipse at 75% 80%, rgba(180,82,28,0.35), transparent 55%),
      radial-gradient(ellipse at 60% 40%, var(--ice), var(--pale-blue) 70%);
  }
  .brain-silhouette {
    position: absolute;
    left: 80px;
    top: 190px;
    width: 665px;
    height: 450px;
  }
  .cover-titles {
    position: absolute;
    left: 0;
    right: 0;
    top: 405px;
    text-align: center;
    font-family: "Orbitron", sans-serif;
    font-weight: 500;
    text-transform: uppercase;
    line-height: 1;
  }
  .album-title {
    margin: 0;
    font-size: 42px;
    letter-spacing: 1px;
    color: var(--title-orange);
    -webkit-text-stroke: 1.5px var(--white);
    paint-order: stroke fill;
  }
  .artist-name {
    margin: 20px 0 0;
    font-size: 40px;
    letter-spacing: 2px;
    color: var(--white);
  }
</style>
</head>
<body>
  <main class="album-cover">
    <div class="neural-backdrop" role="img" aria-label="Abstract web of orange and grey neuron fibres over a pale icy blue field"></div>
    <svg class="brain-silhouette" viewBox="0 0 665 450" role="img" aria-label="Black silhouette of a brain seen from the side">
      <path fill="#121212" d="M60 250 C20 170 80 90 170 80 C220 20 330 10 400 40 C470 20 570 50 600 130 C660 170 670 260 620 320 C600 380 530 400 470 390 C440 440 380 450 350 420 C300 440 230 420 210 380 C130 390 60 340 60 250 Z"/>
    </svg>
    <div class="cover-titles">
      <h1 class="album-title">Quiet Harbors</h1>
      <p class="artist-name">TM Blaze</p>
    </div>
  </main>
</body>
</html>
```